CATALOGUE OF DIAMOND RINGS NEEDED

I have approximately 200 images that need to be designed in a way to be a catalogue. I would firstly like to see a page with about 30 images on it. You can find the images by going to this link; http://velmontrix.com/collection.php?cid=28&tid=33&lang=&page=2 (you may pick any 30 images you like). and then if I like your design of this page, I will invite you through briefharbor to put together the other 6 or 7 pages in a similar way using the other images from this site, and some others. The amount I am paying here, will only be for one page, and then you will be paid more for doing the other pages. you may simply number the products 1,2,3 but have a list on the side of the page that will allow me or you to input details about the item. for example KMT8204 will require information such as $1300. 26 Round Diamonds totaling 0.40 carats.

Colors
86acd3
3377b5
0355a3
cfdfed
86cae6
34a6d7
0493ce
cee9f5

Requirements
Must have
• I really like the look of this catalogue, but it doesn't have to be anything like this. I am open to many different ideas.
• http://ab.pkl.co.za/photos/ballroom/1.jpg

```html
<!DOCTYPE html>
<html lang="en">
<head>
<meta charset="utf-8">
<title>Veradine Jewelry Catalogue 2015</title>
<link href="https://fonts.googleapis.com/css2?family=Great+Vibes&family=Open+Sans:wght@400;700;800&family=Playfair+Display:ital,wght@0,700;1,400&display=swap" rel="stylesheet">
<style>
  :root {
    --backdrop: #ecebe8;
    --plum-deep: #3a0a33;
    --plum: #7a1a68;
    --magenta: #b0187f;
    --lipstick: #d0197f;
    --gold: #e5b43a;
    --gold-light: #f6d77a;
    --gold-dark: #a8741a;
    --yellow: #ffd51f;
    --ink: #1c1016;
    --white: #ffffff;
    --caption: #ffffff;
  }
  * { box-sizing: border-box; margin: 0; padding: 0; }
  html, body { width: 1200px; height: 1013px; overflow: hidden; }
  body { background: var(--backdrop); font-family: "Open Sans", Arial, sans-serif; position: relative; }

  /* ---------- Cover ---------- */
  .cover {
    position: absolute; left: 30px; top: 100px; width: 555px; height: 813px;
    background: radial-gradient(circle at 75% 30%, #b42a92 0%, var(--plum) 45%, var(--plum-deep) 100%);
    overflow: hidden; box-shadow: 0 6px 18px rgba(0,0,0,.25);
  }
  .cover-portrait {
    position: absolute; left: 0; top: 0; width: 300px; height: 690px;
    background: linear-gradient(160deg, #f3d9cc 0%, #e6bca8 45%, #c98f7c 100%);
  }
  .cover-brand {
    position: absolute; left: 330px; top: 60px; display: flex; align-items: center; gap: 10px;
    font-family: "Playfair Display", Georgia, serif; font-weight: 700; font-size: 24px; color: var(--gold);
  }
  .cover-brand .dot { width: 14px; height: 14px; border-radius: 50%; background: var(--gold); }
  .cover-title {
    position: absolute; left: 330px; top: 235px; width: 200px; text-align: center;
    font-weight: 800; color: var(--yellow); font-size: 31px; line-height: 1.1; letter-spacing: .5px;
  }
  .cover-tagline {
    position: absolute; left: 300px; top: 375px; width: 250px; text-align: center;
    font-family: "Playfair Display", Georgia, serif; font-style: italic; color: var(--gold); font-size: 17px;
  }
  .cover-name {
    position: absolute; left: 300px; top: 395px; width: 250px; text-align: center;
    font-family: "Great Vibes", cursive; color: var(--gold-light); font-size: 46px; line-height: 1.2;
  }
  .cover-flourish {
    position: absolute; left: 345px; top: 470px; width: 160px; height: 22px;
    background: linear-gradient(90deg, transparent, var(--gold) 20%, var(--gold-light) 50%, var(--gold) 80%, transparent);
    border-radius: 11px; opacity: .85;
  }
  .cover-footer { position: absolute; left: 0; bottom: 0; width: 100%; height: 200px; }
  .cover-contact {
    position: absolute; right: 30px; bottom: 28px; text-align: right; color: var(--lipstick);
  }
  .cover-contact .phone { font-weight: 800; font-size: 23px; }
  .cover-contact .web { font-weight: 700; font-size: 16px; margin-top: 4px; }

  /* ---------- Product page ---------- */
  .page {
    position: absolute; left: 615px; top: 100px; width: 555px; height: 813px;
    background: var(--ink); padding: 12px; box-shadow: 0 6px 18px rgba(0,0,0,.25);
  }
  .page-frame {
    width: 100%; height: 100%; border: 3px solid var(--gold);
    background: radial-gradient(ellipse at 50% 45%, #a01e84 0%, var(--plum) 45%, var(--plum-deep) 100%);
    padding: 14px 16px; position: relative;
  }
  .page-header { height: 78px; position: relative; }
  .page-name { font-family: "Great Vibes", cursive; color: var(--gold-light); font-size: 44px; line-height: 1; padding-left: 12px; }
  .page-flourish {
    position: absolute; left: 30px; top: 52px; width: 170px; height: 14px; border-radius: 7px;
    background: linear-gradient(90deg, transparent, var(--gold) 25%, var(--gold-light) 50%, var(--gold) 75%, transparent);
  }
  .ring-grid {
    display: grid; grid-template-columns: repeat(5, 1fr); grid-template-rows: repeat(6, 1fr);
    gap: 6px 8px; height: calc(100% - 78px);
  }
  .ring { position: relative; display: flex; flex-direction: column; align-items: center; }
  .ring-number {
    position: absolute; left: 0; top: 0; font-weight: 800; font-size: 14px; color: var(--gold-light);
  }
  .ring-photo {
    width: 66px; height: 50px; margin-top: 6px; border-radius: 50%;
    background: radial-gradient(circle at 45% 40%, #ffffff 0%, #e6e6ea 45%, #b8b8c0 100%);
    border-bottom: 5px solid var(--gold);
  }
  .ring-caption {
    margin-top: 4px; text-align: center; color: var(--caption);
    font-size: 6.5px; line-height: 1.25; font-weight: 700;
  }
</style>
</head>
<body>

<section class="cover">
  <div class="cover-portrait" role="img" aria-label="Fashion portrait of a model with pink lips and green eyes, hand raised showing a large heart-shaped diamond ring"></div>

  <div class="cover-brand"><span class="dot"></span>Veradine</div>

  <h1 class="cover-title">CATALOGUE<br>2015</h1>
  <p class="cover-tagline">World Class Diamond &amp; Jewelry</p>
  <p class="cover-name">Veradine Jewelry</p>
  <div class="cover-flourish" role="img" aria-label="Gold decorative flourish"></div>

  <svg class="cover-footer" viewBox="0 0 555 200" preserveAspectRatio="none" aria-hidden="true">
    <defs>
      <linearGradient id="goldBand" x1="0" y1="0" x2="1" y2="0">
        <stop offset="0" stop-color="#a8741a"/>
        <stop offset=".5" stop-color="#f6d77a"/>
        <stop offset="1" stop-color="#c48d24"/>
      </linearGradient>
    </defs>
    <path d="M0 90 C160 40 360 10 555 20 L555 200 L0 200 Z" fill="url(#goldBand)"/>
    <path d="M0 112 C170 60 370 38 555 45 L555 200 L0 200 Z" fill="#ffffff"/>
  </svg>

  <div class="cover-contact">
    <p class="phone">Call : 000-987-654-321</p>
    <p class="web">www.veradinejewelry.com</p>
  </div>
</section>

<section class="page">
  <div class="page-frame">
    <header class="page-header">
      <p class="page-name">Veradine Jewelry</p>
      <div class="page-flourish" role="img" aria-label="Gold decorative flourish"></div>
    </header>
    <div class="ring-grid">
      <div class="ring"><span class="ring-number">1.</span><div class="ring-photo" role="img" aria-label="Diamond ring on gold display stand"></div><p class="ring-caption">$1300 26 Round<br>Diamonds<br>totaling 0.40 Carats</p></div>
      <div class="ring"><span class="ring-number">2.</span><div class="ring-photo" role="img" aria-label="Diamond ring on gold display stand"></div><p class="ring-caption">$1300 26 Round<br>Diamonds<br>totaling 0.40 Carats</p></div>
      <div class="ring"><span class="ring-number">3.</span><div class="ring-photo" role="img" aria-label="Diamond ring on gold display stand"></div><p class="ring-caption">$1300 26 Round<br>Diamonds<br>totaling 0.40 Carats</p></div>
      <div class="ring"><span class="ring-number">4.</span><div class="ring-photo" role="img" aria-label="Diamond ring on gold display stand"></div><p class="ring-caption">$1300 26 Round<br>Diamonds<br>totaling 0.40 Carats</p></div>
      <div class="ring"><span class="ring-number">5.</span><div class="ring-photo" role="img" aria-label="Diamond ring on gold display stand"></div><p class="ring-caption">$1300 26 Round<br>Diamonds<br>totaling 0.40 Carats</p></div>
      <div class="ring"><span class="ring-number">6.</span><div class="ring-photo" role="img" aria-label="Diamond ring on gold display stand"></div><p class="ring-caption">$1300 26 Round<br>Diamonds<br>totaling 0.40 Carats</p></div>
      <div class="ring"><span class="ring-number">7.</span><div class="ring-photo" role="img" aria-label="Diamond ring on gold display stand"></div><p class="ring-caption">$1300 26 Round<br>Diamonds<br>totaling 0.40 Carats</p></div>
      <div class="ring"><span class="ring-number">8.</span><div class="ring-photo" role="img" aria-label="Diamond ring on gold display stand"></div><p class="ring-caption">$1300 26 Round<br>Diamonds<br>totaling 0.40 Carats</p></div>
      <div class="ring"><span class="ring-number">9.</span><div class="ring-photo" role="img" aria-label="Diamond ring on gold display stand"></div><p class="ring-caption">$1300 26 Round<br>Diamonds<br>totaling 0.40 Carats</p></div>
      <div class="ring"><span class="ring-number">10.</span><div class="ring-photo" role="img" aria-label="Diamond ring on gold display stand"></div><p class="ring-caption">$1300 26 Round<br>Diamonds<br>totaling 0.40 Carats</p></div>
      <div class="ring"><span class="ring-number">11.</span><div class="ring-photo" role="img" aria-label="Diamond ring on gold display stand"></div><p class="ring-caption">$1300 26 Round<br>Diamonds<br>totaling 0.40 Carats</p></div>
      <div class="ring"><span class="ring-number">12.</span><div class="ring-photo" role="img" aria-label="Diamond ring on gold display stand"></div><p class="ring-caption">$1300 26 Round<br>Diamonds<br>totaling 0.40 Carats</p></div>
      <div class="ring"><span class="ring-number">13.</span><div class="ring-photo" role="img" aria-label="Diamond ring on gold display stand"></div><p class="ring-caption">$1300 26 Round<br>Diamonds<br>totaling 0.40 Carats</p></div>
      <div class="ring"><span class="ring-number">14.</span><div class="ring-photo" role="img" aria-label="Diamond ring on gold display stand"></div><p class="ring-caption">$1300 26 Round<br>Diamonds<br>totaling 0.40 Carats</p></div>
      <div class="ring"><span class="ring-number">15.</span><div class="ring-photo" role="img" aria-label="Diamond ring on gold display stand"></div><p class="ring-caption">$1300 26 Round<br>Diamonds<br>totaling 0.40 Carats</p></div>
      <div class="ring"><span class="ring-number">16.</span><div class="ring-photo" role="img" aria-label="Diamond ring on gold display stand"></div><p class="ring-caption">$1300 26 Round<br>Diamonds<br>totaling 0.40 Carats</p></div>
      <div class="ring"><span class="ring-number">17.</span><div class="ring-photo" role="img" aria-label="Diamond ring on gold display stand"></div><p class="ring-caption">$1300 26 Round<br>Diamonds<br>totaling 0.40 Carats</p></div>
      <div class="ring"><span class="ring-number">18.</span><div class="ring-photo" role="img" aria-label="Diamond ring on gold display stand"></div><p class="ring-caption">$1300 26 Round<br>Diamonds<br>totaling 0.40 Carats</p></div>
      <div class="ring"><span class="ring-number">19.</span><div class="ring-photo" role="img" aria-label="Diamond ring on gold display stand"></div><p class="ring-caption">$1300 26 Round<br>Diamonds<br>totaling 0.40 Carats</p></div>
      <div class="ring"><span class="ring-number">20.</span><div class="ring-photo" role="img" aria-label="Diamond ring on gold display stand"></div><p class="ring-caption">$1300 26 Round<br>Diamonds<br>totaling 0.40 Carats</p></div>
      <div class="ring"><span class="ring-number">21.</span><div class="ring-photo" role="img" aria-label="Diamond ring on gold display stand"></div><p class="ring-caption">$1300 26 Round<br>Diamonds<br>totaling 0.40 Carats</p></div>
      <div class="ring"><span class="ring-number">22.</span><div class="ring-photo" role="img" aria-label="Diamond ring on gold display stand"></div><p class="ring-caption">$1300 26 Round<br>Diamonds<br>totaling 0.40 Carats</p></div>
      <div class="ring"><span class="ring-number">23.</span><div class="ring-photo" role="img" aria-label="Diamond ring on gold display stand"></div><p class="ring-caption">$1300 26 Round<br>Diamonds<br>totaling 0.40 Carats</p></div>
      <div class="ring"><span class="ring-number">24.</span><div class="ring-photo" role="img" aria-label="Diamond ring on gold display stand"></div><p class="ring-caption">$1300 26 Round<br>Diamonds<br>totaling 0.40 Carats</p></div>
      <div class="ring"><span class="ring-number">25.</span><div class="ring-photo" role="img" aria-label="Diamond ring on gold display stand"></div><p class="ring-caption">$1300 26 Round<br>Diamonds<br>totaling 0.40 Carats</p></div>
      <div class="ring"><span class="ring-number">26.</span><div class="ring-photo" role="img" aria-label="Diamond ring on gold display stand"></div><p class="ring-caption">$1300 26 Round<br>Diamonds<br>totaling 0.40 Carats</p></div>
      <div class="ring"><span class="ring-number">27.</span><div class="ring-photo" role="img" aria-label="Diamond ring on gold display stand"></div><p class="ring-caption">$1300 26 Round<br>Diamonds<br>totaling 0.40 Carats</p></div>
      <div class="ring"><span class="ring-number">28.</span><div class="ring-photo" role="img" aria-label="Diamond ring on gold display stand"></div><p class="ring-caption">$1300 26 Round<br>Diamonds<br>totaling 0.40 Carats</p></div>
      <div class="ring"><span class="ring-number">29.</span><div class="ring-photo" role="img" aria-label="Diamond ring on gold display stand"></div><p class="ring-caption">$1300 26 Round<br>Diamonds<br>totaling 0.40 Carats</p></div>
      <div class="ring"><span class="ring-number">30.</span><div class="ring-photo" role="img" aria-label="Diamond ring on gold display stand"></div><p class="ring-caption">$1300 26 Round<br>Diamonds<br>totaling 0.40 Carats</p></div>
    </div>
  </div>
</section>

</body>
</html>
```